Computer consultant website

Vexlo Software is a newly started computer consulting company. It's a small one-man company that provides mostly Android applications but also websites in collaboration with designers. I'm running this company on the side of full time university studies.

I'm in need of a website which will function as:
Primarily - I'll direct potential clients to the page so they can read about the company, what i offer and past work.
Secondarily - Making my company visible through the web and maybe getting new clients.

The final design should look modern, clean and professional.

Pages that will be in the final website are (Note that it's not the exact titles as the page will not be in english):
* About
* Services (what Vexlo offers)
* Portfolio/work
* Short news (like PlanHives "News and press")
* Contact.

Inspiration
http://www.planhive.example/design/87836
http://www.brambleorb.example/
http://www.planhive.example/design/845881
http://www.planhive.example/design/1369424 - Lighter design, however a bit cluttered.

No programming code is needed delivered at all. Focus on designing rather then coding.

If you have any questions, do not hesitate to send me a message.

Target Market(s)

Non-technical entrepreneurs and small companies.

Industry/Entity Type

University

Requirements
Must have
• Must have my company logo (see attachment).

Must in any way use both colors from my logo.

A way to logically rearrange content to fit smaller screens. I will implement this design so that it can be pleasantly viewed on mobile devices. You don't necessarily need to provide exactly how the design would look on mobile devices.

I need the following types of page designs:
* Landing page
* Content page
* Portfolio/work (with accompanying inside/clicked) page

Landing/start page must in any way include at least the information:
* Shorter version of "About Vexlo"
* At least 1 most recent portfolio/work entry
* At least 1 most recent news entry
* Services that Vexlo offers.
Nice to have
Should not have
• Testimonials or newsletter.

```html
<!DOCTYPE html>
<html lang="en">
<head>
<meta charset="utf-8">
<title>Vexlo Software</title>
<link rel="stylesheet" href="https://fonts.googleapis.com/css2?family=Noto+Sans:wght@400;500&family=Questrial&display=swap">
<style>
  :root {
    --brand-blue: #1e6fd0;
    --brand-dark: #333333;
    --heading-blue: #1d5aa3;
    --ink: #111111;
    --muted: #555555;
    --page-sky: #e6f0fb;
    --page-light: #f7fbff;
    --band-dark: #3a3a3a;
    --footer-black: #0d0d0d;
    --footer-text: #cfcfcf;
    --white: #ffffff;
  }
  * { box-sizing: border-box; margin: 0; padding: 0; }
  html, body { width: 1200px; height: 1000px; overflow: hidden; }
  body {
    position: relative;
    font-family: "Noto Sans", sans-serif;
    color: var(--ink);
    background:
      linear-gradient(150deg, transparent 55%, rgba(120,170,230,.25) 70%, transparent 85%),
      linear-gradient(30deg, rgba(120,170,230,.35) 0%, transparent 30%),
      linear-gradient(180deg, var(--page-light), var(--page-sky));
  }
  .site { position: absolute; left: 148px; top: 0; width: 900px; height: 1000px; }

  /* Header */
  .site-header {
    position: absolute; left: 0; top: 0; width: 900px; height: 51px;
    background: linear-gradient(90deg, #d8d8d8 0%, #8a8a8a 8%, #1a1a1a 22%, #000 40%);
  }
  .brand { position: absolute; left: 12px; top: 2px; display: flex; align-items: center; gap: 8px; }
  .brand-mark { width: 40px; height: 40px; border-radius: 50%; background: var(--brand-blue); }
  .brand-name { font-family: "Questrial", sans-serif; font-size: 40px; color: var(--brand-dark); line-height: 44px; }
  .main-nav { position: absolute; right: 0; top: 24px; display: flex; height: 27px; }
  .main-nav a {
    font-family: "Questrial", sans-serif; font-size: 15px; color: var(--white);
    text-decoration: none; text-transform: uppercase; line-height: 28px; padding: 0 10.5px;
  }
  .main-nav a.is-active { background: var(--brand-blue); padding: 0 12px; }

  /* Hero */
  .hero {
    position: absolute; left: 0; top: 51px; width: 900px; height: 311px;
    background:
      radial-gradient(ellipse at 30% 40%, rgba(255,255,255,.45), transparent 45%),
      radial-gradient(ellipse at 80% 55%, rgba(20,20,30,.55), transparent 30%),
      linear-gradient(180deg, #2f7ed8 0%, #4a95e4 55%, #6aa9ea 100%);
  }

  /* Content columns */
  .intro {
    position: absolute; left: 0; top: 362px; width: 900px; height: 334px;
    background: linear-gradient(180deg, #e4e4e4 0%, #ffffff 40%, #f6f6f6 100%);
  }
  .col { position: absolute; top: 18px; width: 210px; height: 310px; }
  .col h2 { font-weight: 400; font-size: 18px; color: var(--heading-blue); margin-bottom: 11px; }
  .col p { font-size: 14.4px; line-height: 17px; margin-bottom: 16px; }
  .col .date { margin-bottom: 11px; }
  .more {
    position: absolute; top: 303px; font-size: 13px; color: var(--muted); text-decoration: underline;
  }

  /* Clients */
  .clients {
    position: absolute; left: 0; top: 696px; width: 900px; height: 124px;
    background: linear-gradient(180deg, #2e2e2e, #4a4a4a);
  }
  .clients h2 { position: absolute; left: 21px; top: 13px; font-weight: 400; font-size: 17px; color: var(--white); }
  .client {
    position: absolute; display: flex; align-items: center; justify-content: center; gap: 6px;
    font-size: 14px; font-weight: 500; color: #222;
  }
  .client.boxed { background: var(--white); }
  .client .dot { width: 12px; height: 12px; border-radius: 50%; }

  /* Footer */
  .site-footer {
    position: absolute; left: 0; top: 820px; width: 900px; height: 180px;
    background: linear-gradient(180deg, #000 0%, #1c1c1c 60%, #2a2a2a 100%);
  }
  .footer-col { position: absolute; top: 16px; width: 190px; font-size: 9.6px; color: var(--footer-text); line-height: 12px; }
  .footer-col p { margin-bottom: 11px; }
  .footer-col p:first-child { margin-bottom: 14px; }
  .footer-nav { position: absolute; top: 164px; width: 900px; text-align: center; }
  .footer-nav a {
    font-family: "Questrial", sans-serif; font-size: 9px; color: var(--white);
    text-decoration: none; text-transform: uppercase; margin: 0 3px;
  }
</style>
</head>
<body>
<div class="site">
  <header class="site-header">
    <div class="brand"><span class="brand-mark"></span><span class="brand-name">Vexlo</span></div>
    <nav class="main-nav">
      <a class="is-active" href="#">Home</a>
      <a href="#">About us</a>
      <a href="#">Services</a>
      <a href="#">Portfolio</a>
      <a href="#">Short news</a>
      <a href="#">Contact</a>
    </nav>
  </header>

  <div class="hero" role="img" aria-label="Hero photo: a consultant touching a floating cloud screen beside an open laptop, on a blue sky background"></div>

  <section class="intro">
    <div class="col" style="left:12px">
      <h2>About us</h2>
      <p>Lorem ipsum dolor sit amet, consectetuer adipiscing elit, sed diam nonummy nibh euismod tincidunt ut laoreet dolore magna aliquam erat volutpat. Ut wisi enim ad minim veniam, quis nostrud exerci tation ullamcorper suscipit lobortis nisl ut aliquip ex ea commodo consequat.</p>
    </div>
    <a class="more" href="#" style="left:158px">more</a>

    <div class="col" style="left:244px">
      <h2>Services</h2>
      <p>Lorem ipsum dolor sit amet, consectetuer</p>
      <p>Duis autem vel eum iriure dolor in hendrerit in vulputate</p>
      <p>Typi non habent claritatem insitam</p>
      <p>Eodem modo typi, qui nunc nobis videntur parum clari,</p>
      <p>fiant sollemnes in futurum.</p>
    </div>
    <a class="more" href="#" style="left:412px">more</a>

    <div class="col" style="left:468px">
      <h2>News</h2>
      <p class="date">12.02.13</p>
      <p>Lorem ipsum dolor sit amet</p>
      <p class="date">12.02.13</p>
      <p>Lorem ipsum dolor sit amet</p>
      <p class="date">12.02.13</p>
      <p>Lorem ipsum dolor sit amet</p>
      <p class="date">12.02.13</p>
      <p>Lorem ipsum dolor sit amet</p>
    </div>
    <a class="more" href="#" style="left:634px">more</a>

    <div class="col" style="left:689px">
      <h2>Recent Jobs</h2>
      <p>Lorem ipsum dolor sit amet, consectetuer</p>
      <p>Duis autem vel eum iriure dolor in hendrerit in vulputate</p>
      <p>Typi non habent claritatem insitam</p>
    </div>
    <a class="more" href="#" style="left:846px">more</a>
  </section>

  <section class="clients">
    <h2>Our Clients</h2>
    <div class="client boxed" style="left:19px;top:48px;width:89px;height:57px">Norvane</div>
    <div class="client boxed" style="left:124px;top:48px;width:125px;height:57px">Pellgrove</div>
    <div class="client boxed" style="left:265px;top:47px;width:98px;height:59px">Tarsel Group</div>
    <div class="client" style="left:388px;top:60px;width:100px;height:30px;color:var(--white)"><span class="dot" style="background:#d8202a"></span>Quillon</div>
    <div class="client boxed" style="left:514px;top:45px;width:76px;height:60px;font-size:12px">Yarrow Co</div>
    <div class="client boxed" style="left:628px;top:45px;width:123px;height:61px">Dunmere</div>
    <div class="client" style="left:770px;top:58px;width:112px;height:34px;color:var(--white)"><span class="dot" style="background:#e8892a"></span>Kestrel</div>
  </section>

  <footer class="site-footer">
    <div class="footer-col" style="left:34px">
      <p>Lorem ipsum</p>
      <p>Lorem ipsum dolor sit amet, consectetuer</p>
      <p>Duis autem vel eum iriure dolor in hendrerit in vulputate</p>
      <p>Typi non habent claritatem insitam</p>
    </div>
    <div class="footer-col" style="left:261px">
      <p>Lorem ipsum</p>
      <p>Lorem ipsum dolor sit amet, consectetuer</p>
      <p>Duis autem vel eum iriure dolor in hendrerit in vulputate</p>
      <p>Typi non habent claritatem insitam</p>
    </div>
    <div class="footer-col" style="left:491px">
      <p>Lorem ipsum</p>
      <p>Lorem ipsum dolor sit amet, consectetuer</p>
      <p>Duis autem vel eum iriure dolor in hendrerit in vulputate</p>
      <p>Typi non habent claritatem insitam</p>
    </div>
    <div class="footer-col" style="left:710px">
      <p>Lorem ipsum</p>
      <p>Lorem ipsum dolor sit amet, consectetuer</p>
      <p>Duis autem vel eum iriure dolor in hendrerit in vulputate</p>
      <p>Typi non habent claritatem insitam</p>
    </div>
    <nav class="footer-nav">
      <a href="#">Home</a>
      <a href="#">About us</a>
      <a href="#">Services</a>
      <a href="#">Portfolio</a>
      <a href="#">Short news</a>
      <a href="#">Contact</a>
    </nav>
  </footer>
</div>
</body>
</html>
```